Wellmere Talking Therapies Hub

We need a design for magazine advert, ideally high resolution to advertise our counselling centre. we would like this to include a photo of two people talking, as if in a counselling session. See our logo and colour range on our website. www.wtth-brackly.co.uk
The photo should not include cups of coffee, clipboards, desks, people touching. it needs to be two people in armchairs sympathetically listening and looking at each other.
The font type is Great Vibes on the logo. Our design should communicate a centre of excellence delivering high quality, professional services in stylishly furnished surroundings.
Updates

Hello Everyone We have had a number of designs that look quite promising but are missing the brief. Can I reiterate that we need a photograph of 2 people seated talking to each other in a sincere way. There shouldn't be office chairs but comfortable chairs. There should be no physical contact. There should be no clipboards.Thank you very muchHeather Added Sunday, March 12, 2017

Target Market(s)

people seeking counselling and psychotherapy

Font styles to use
Other font styles liked:
• Great Vibes as in our logo for some of the print. See attached file.

Requirements
Must have
• good photograph
• Two high res Pixelmarsh photos:
• https://pixelmarsh-files.example-dl.net/attach/get?id=QX81mvB7kTzRwe%2F9PoLnA4Hy%2BdS2cUfjGh0ZrtVbNq6xKe5MsiWoYp3LaDf8TgHu%2BjEw7Rc1Xn%3D%3D
• https://pixelmarsh-files.example-dl.net/attach/get?id=QX81mvB7kTzRwe%2F9PoLnB5Jz%2BeT3dVgkHi1AsuWcOr7yLf6NtjXpZq4MbEg9UhIv%2BkFx8Sd2Yo%3D%3D
Nice to have
• Watermark in keeping with our logo.
Should not have
• Darkness

```html
<!DOCTYPE html>
<html lang="en">
<head>
<meta charset="utf-8">
<title>Wellmere Talking Therapies Hub – Magazine Advert</title>
<link rel="stylesheet" href="https://fonts.googleapis.com/css2?family=Great+Vibes&family=Montserrat:wght@400;500;600&display=swap">
<style>
  :root {
    --page-bg: #e9e9e9;
    --cream: #f3ede0;
    --sage: #a9bd8c;
    --olive: #7d9a2e;
    --phone-green: #8fae6a;
    --brown: #3b3030;
    --ink: #2b2424;
    --white: #ffffff;
  }
  * { margin: 0; padding: 0; box-sizing: border-box; }
  html, body { width: 1200px; height: 1200px; overflow: hidden; }
  body {
    background: var(--page-bg);
    font-family: "Montserrat", Arial, sans-serif;
    position: relative;
  }
  .advert {
    position: absolute;
    left: 211px;
    top: 50px;
    width: 778px;
    height: 1100px;
    background: var(--cream);
    overflow: hidden;
    box-shadow: 0 18px 40px rgba(0,0,0,0.18);
  }
  .advert-shapes { position: absolute; inset: 0; width: 100%; height: 100%; }
  .headline {
    position: absolute;
    left: 0; right: 0;
    top: 495px;
    text-align: center;
    font-family: "Great Vibes", cursive;
    font-size: 50px;
    line-height: 58px;
    color: var(--ink);
  }
  .intro {
    position: absolute;
    left: 162px;
    top: 664px;
    width: 330px;
    font-size: 16.5px;
    line-height: 23px;
    color: var(--ink);
  }
  .intro strong { color: var(--olive); font-weight: 600; }
  .contact {
    position: absolute;
    left: 63px;
    top: 912px;
    color: var(--white);
  }
  .contact-hours { font-size: 14px; line-height: 17px; }
  .contact-phone {
    font-size: 31px;
    line-height: 38px;
    color: var(--phone-green);
    letter-spacing: 0.5px;
  }
  .contact-address { font-size: 14px; line-height: 17px; margin-top: 8px; }
  .contact-web { font-size: 14.5px; font-weight: 600; margin-top: 16px; }
  .brand {
    position: absolute;
    left: 380px;
    top: 900px;
    width: 340px;
    text-align: center;
  }
  .brand-dot {
    width: 44px; height: 44px;
    border-radius: 50%;
    background: var(--sage);
    margin: 0 auto 18px;
  }
  .brand-name {
    font-family: "Great Vibes", cursive;
    font-size: 36px;
    line-height: 40px;
    color: var(--ink);
  }
</style>
</head>
<body>
  <div class="advert">
    <svg class="advert-shapes" viewBox="0 0 778 1100" xmlns="http://www.w3.org/2000/svg">
      <defs>
        <linearGradient id="session-photo-tone" x1="0" y1="0" x2="1" y2="1">
          <stop offset="0" stop-color="#4f5f3c"/>
          <stop offset="0.45" stop-color="#6d7a56"/>
          <stop offset="0.7" stop-color="#8fa07c"/>
          <stop offset="1" stop-color="#4a4a48"/>
        </linearGradient>
        <linearGradient id="therapists-photo-tone" x1="0" y1="0" x2="1" y2="0">
          <stop offset="0" stop-color="#e6e3e2"/>
          <stop offset="0.5" stop-color="#e2c7c0"/>
          <stop offset="1" stop-color="#b9d8d0"/>
        </linearGradient>
      </defs>
      <path class="accent-band" fill="#a9bd8c" d="M0 575 C120 510 260 490 440 470 C610 450 720 390 778 285 V255 C700 380 600 430 450 455 C250 480 100 500 0 555 Z"/>
      <g role="img" aria-label="Photo of a counsellor listening to a young man in a camouflage jacket, both seated in armchairs by a window">
        <path fill="url(#session-photo-tone)" d="M0 0 H778 V255 C700 380 600 430 450 455 C250 480 100 500 0 555 Z"/>
      </g>
      <path class="white-corner" fill="#ffffff" d="M330 1100 C390 1000 410 880 520 842 C620 812 720 800 778 792 V1100 Z"/>
      <g role="img" aria-label="Photo of two smiling female therapists seated in a bright consulting room">
        <path fill="url(#therapists-photo-tone)" d="M412 836 C480 720 600 660 778 612 V792 C720 800 620 812 520 842 C470 858 440 860 412 836 Z"/>
      </g>
      <path class="contact-panel" fill="#3b3030" d="M0 925 C120 860 280 822 420 832 C385 900 380 1000 330 1100 H0 Z"/>
    </svg>

    <h1 class="headline">Confidential Therapeutic Services<br>in the Heart of Old Town</h1>

    <p class="intro">We have over <strong>30 carefully selected, qualified and professional therapists</strong> offering a range of services to help individuals, families and couples.</p>

    <div class="contact">
      <p class="contact-hours">Appointments available<br>throughout the day and evening</p>
      <p class="contact-phone">01632 960418</p>
      <p class="contact-address">14 Mill Lane, Old Town,<br>Brackly BK2 7QT</p>
      <p class="contact-web">www.wtth-brackly.co.uk</p>
    </div>

    <div class="brand">
      <div class="brand-dot"></div>
      <p class="brand-name">Wellmere Talking Therapies Hub</p>
    </div>
  </div>
</body>
</html>
```